Hartwell Systems Advisory - IT Consultancy

I already have a Wordpress site, but not happy with the look and feel or the template I chose.
I want a site as a web presence only, I can configure base SEO myself, but most business is referrals not from a search, so low priority.

My current site is http://hartsys.example where you can see the sort of content I already have.

Target Market(s)

Business to Business services.

Industry/Entity Type

Consulting

Font styles to use
Sans Serif

Colors
3277b5

Requirements
Must have
• Front Page Template
• Freephone number on front page.
• My Logo and the Brevanta logo on the front page
• Page template for Services, Solutions and Portfolio
• Contact Page
• Ability to embed links to Video clips hosted by a third party
Nice to have
• Each page could have a side bar with some common functions, like Request Demo.
• Second Contact Page specifically to Request Demonstrations of Brevanta Products, the demo contact page needs to capture some additional information in text boxes and also a check box list of features. The list of features needs to be easily configurable.
• Features to include in checkbox list.
• Contract Management
• Service Desk
• Document Management
• Contract Management
• Business Workflow

```html
<!DOCTYPE html>
<html lang="en">
<head>
<meta charset="utf-8">
<title>Project Management – Hartwell Systems Advisory</title>
<link href="https://fonts.googleapis.com/css2?family=Cabin:wght@400;500;600;700&family=Lato:wght@300;400;700&display=swap" rel="stylesheet">
<style>
:root{
  --brand:#3277b5;
  --brand-deep:#2a64a6;
  --ink:#2b2f36;
  --muted:#8a8f96;
  --night:#0f1726;
  --night-2:#0c1a2d;
  --night-3:#0a1322;
  --white:#ffffff;
  --line:#2c5fa0;
}
*{margin:0;padding:0;box-sizing:border-box}
html,body{width:683px;height:1200px;overflow:hidden;background:var(--night-3)}
body{position:relative;font-family:"Lato",sans-serif;color:var(--ink)}
.abs{position:absolute}

/* header */
.site-header{left:0;top:0;width:683px;height:63px;background:var(--white)}
.brand{left:52px;top:20px;font-family:"Cabin",sans-serif;font-weight:600;font-size:19px;color:var(--brand);letter-spacing:1px;line-height:1}
.brand small{display:block;font-family:"Lato",sans-serif;font-weight:400;font-size:6px;letter-spacing:.6px;margin-top:5px}
.brand-divider{left:154px;top:17px;width:1px;height:34px;background:#e4e6ea}
.partner{left:163px;top:24px;font-family:"Cabin",sans-serif;font-weight:700;font-size:15px;color:var(--brand)}
.partner small{display:block;font-size:6px;font-weight:600;text-align:right}
.topline{left:297px;top:20px;font-size:6.5px;color:#999}
.topline b{color:#666}
.topline .sep{display:inline-block;width:1px;height:12px;background:#ddd;vertical-align:middle;margin:0 9px}
.topline a{color:var(--brand);text-decoration:none}
.social{left:587px;top:20px;display:flex;gap:3px}
.social span{width:8px;height:8px;background:var(--brand)}
.nav{left:273px;top:38px;display:flex;align-items:center;font-size:6.5px;font-weight:700;color:#222;letter-spacing:.1px}
.nav span{margin-left:16px}
.nav .active{color:var(--brand);position:relative}
.nav .active::after{content:"";position:absolute;left:0;top:11px;width:8px;height:1.5px;background:var(--brand)}

/* hero */
.hero{left:0;top:63px;width:683px;height:101px;background:linear-gradient(90deg,#1c3a66 0%,#12284a 45%,#183760 75%,#0f2444 100%)}
.hero-kicker{left:0;top:96px;width:683px;text-align:center;color:#e6ecf5;font-size:9px;letter-spacing:1.2px}
.hero-title{left:0;top:112px;width:683px;text-align:center;color:var(--white);font-family:"Cabin",sans-serif;font-weight:700;font-size:24px;letter-spacing:.5px}

/* intro */
.intro{left:52px;top:204px;width:396px;font-size:9px;line-height:13px;color:var(--muted);font-weight:300}
.intro .dropcap{float:left;font-family:"Cabin",sans-serif;font-weight:700;color:var(--brand);font-size:31px;line-height:26px;margin:2px 6px 0 0}
.intro b{font-weight:700;color:#6a6f76}
.intro p+p{margin-top:12px;clear:both}

/* dark content */
.dark{left:0;top:297px;width:683px;height:505px;background:radial-gradient(ellipse at 85% 55%,#1b2433 0%,#101825 55%,#0d1420 100%)}
.section-title{font-family:"Cabin",sans-serif;font-weight:600;color:var(--brand);font-size:18px}
.project{width:200px;height:49px;border:1px solid var(--line);display:flex;align-items:center;color:var(--white);font-family:"Cabin",sans-serif;font-weight:500;font-size:9px;line-height:13px}
.project svg{width:30px;height:26px;margin:0 25px 0 14px;flex:none}
.list{list-style:none;color:var(--white);font-size:9px;line-height:15px}
.list li{position:relative;padding-left:14px}
.list li::before{content:"";position:absolute;left:1px;top:6px;width:3px;height:3px;border-radius:50%;background:#9aa3ad}

/* demo form */
.demo{left:483px;top:195px;width:146px;height:314px;background:linear-gradient(160deg,#3a80c4,#2a64a6)}
.demo h3{position:absolute;left:0;top:20px;width:146px;text-align:center;color:var(--white);font-family:"Cabin",sans-serif;font-weight:600;font-size:12px}
.demo .lead{position:absolute;left:14px;top:50px;width:122px;color:#e8f0fa;font-size:6.5px;line-height:11px}
.demo-card{position:absolute;left:13px;top:83px;width:120px;height:216px;background:var(--white)}
.field{position:absolute;left:10px;width:99px;height:15px;border-bottom:1px solid #333;font-size:6.5px;color:#bbb}
.field .caret{position:absolute;right:0;top:-11px;width:8px;height:25px;border:1px solid #bbb;background:#f4f4f4}
.demo-note{position:absolute;left:10px;top:106px;width:102px;text-align:center;font-size:6.5px;line-height:11px;color:#777}
.demo-btn{position:absolute;left:10px;top:173px;width:99px;height:26px;background:var(--brand);color:var(--white);font-family:"Cabin",sans-serif;font-weight:700;font-size:6.5px;text-align:center;line-height:26px;letter-spacing:.2px}

/* contact band */
.contact{left:0;top:802px;width:683px;height:116px;background:var(--night-2)}
.contact-item{position:absolute;top:46px}
.contact-item i{display:block;font-size:7px;color:#8c96a4}
.contact-item strong{display:block;margin-top:6px;color:var(--white);font-family:"Cabin",sans-serif;font-weight:600;font-size:12px}
.contact-item span{display:block;margin-top:7px;font-size:7px;color:#8c96a4}
.contact-item a{display:block;margin-top:7px;font-size:7px;color:var(--brand);text-decoration:none}

/* footer */
.footer{left:0;top:918px;width:683px;height:282px;background:var(--night-3)}
.foot-brand{left:54px;top:960px;font-family:"Cabin",sans-serif;font-weight:600;font-size:19px;color:var(--brand-deep);letter-spacing:1px;line-height:1}
.foot-brand small{display:block;font-family:"Lato",sans-serif;font-size:6px;letter-spacing:.6px;margin-top:5px}
.foot-about{left:54px;top:1001px;width:120px;font-size:6.5px;line-height:12px;color:#7d8692}
.foot-h{font-size:8px;color:#e6ebf2}
.foot-text{font-size:6.5px;line-height:12px;color:#7d8692}
.foot-text .hi{color:#cfd6df;padding-left:17px;display:block}
.links{list-style:none;font-size:6.5px;line-height:12px;color:#7d8692}
.links li::before{content:"→";margin-right:7px}
.news{display:flex;gap:6px;margin-bottom:7px}
.news .date{width:28px;height:20px;background:var(--white);font-size:6.5px;font-weight:700;color:#111;padding:2px 3px;line-height:8px}
.news .date small{display:block;font-weight:400;font-size:5px}
.news p{font-size:6.5px;line-height:12px;color:#7d8692;width:100px}
.copyright{left:52px;top:1129px;font-size:6.5px;color:#7d8692}
.badge{background:#e8ebef;border-radius:2px}
</style>
</head>
<body>

<header class="abs site-header"></header>
<div class="abs brand">HARTWELL<small>SYSTEMS ADVISORY</small></div>
<div class="abs brand-divider"></div>
<div class="abs partner">Brevanta<small>Gold Partner</small></div>
<div class="abs topline"><b>Phone :</b> +44 (0) 80 00 55 50 12<span class="sep"></span><a>Request Demostrations Services</a></div>
<div class="abs social"><span></span><span></span><span></span><span></span></div>
<nav class="abs nav">
  <svg width="8" height="8" viewBox="0 0 10 10"><circle cx="4" cy="4" r="3" fill="none" stroke="#444" stroke-width="1.3"/><line x1="6.3" y1="6.3" x2="9.3" y2="9.3" stroke="#444" stroke-width="1.3"/></svg>
  <span>HOME</span><span class="active">SERVICES</span><span>BREVANTA SOLUTIONS</span><span>PORTFOLIO</span><span>CLIENTS</span><span>BLOG</span><span>CONTACT US</span>
</nav>

<div class="abs hero" role="img" aria-label="Hand touching a network of glowing gears in blue tones"></div>
<div class="abs hero-kicker">SERVICES</div>
<h1 class="abs hero-title">Project Management</h1>

<div class="abs intro">
  <p><span class="dropcap">C</span><b>Hartwell Systems Advisory</b> has many years experience managing projects from a few weeks with budget of thousands to projects spanning years with budgets of millions.</p>
  <p>With experience with both Waterfall and Agile techniques, we can ensure the most appropriate Project Management tools are used for your project.</p>
</div>

<section class="abs dark" role="img" aria-label="Dark blue background with faint gears, network lines and a hand"></section>

<h2 class="abs section-title" style="left:52px;top:325px">Projects</h2>
<div class="abs project" style="left:52px;top:364px">
  <svg viewBox="0 0 30 26"><rect x="1" y="3" width="27" height="21" fill="none" stroke="#3a86d6" stroke-width="2"/><rect x="1" y="3" width="27" height="5" fill="#3a86d6"/><circle cx="14.5" cy="15.5" r="4" fill="#3a86d6"/></svg>
  Software development, managing development, QA, UX teams</div>
<div class="abs project" style="left:260px;top:364px">
  <svg viewBox="0 0 30 26"><ellipse cx="12" cy="5" rx="10" ry="4" fill="#3a86d6"/><rect x="2" y="5" width="20" height="14" fill="#3a86d6"/><circle cx="20" cy="19" r="6" fill="#2a64a6"/><path d="M20 16v7M17 19l3-3 3 3" stroke="#fff" stroke-width="1.5" fill="none"/></svg>
  Data Centre Build Projects, managing Server, Storage and Networks teams</div>
<div class="abs project" style="left:52px;top:421px">
  <svg viewBox="0 0 30 26"><path d="M4 6h7a3 3 0 1 1 6 0h7v7a3 3 0 1 1 0 6v6H4z" fill="#3a86d6"/></svg>
  Third Party COTS Package Implementation</div>
<div class="abs project" style="left:260px;top:421px">
  <svg viewBox="0 0 30 26"><circle cx="10" cy="16" r="7" fill="#3a86d6"/><circle cx="10" cy="16" r="2.5" fill="#101825"/><circle cx="23" cy="7" r="5" fill="#3a86d6"/><circle cx="23" cy="7" r="1.8" fill="#101825"/></svg>
  SaaS Service Implementation</div>
<div class="abs project" style="left:52px;top:479px">
  <svg viewBox="0 0 30 26"><path d="M15 12l11 5-11 5-11-5z" fill="#3a86d6"/><path d="M4 14l11 5 11-5" fill="none" stroke="#3a86d6" stroke-width="1.5"/><path d="M8 4l-3 3 3 3M22 4l3 3-3 3" fill="none" stroke="#3a86d6" stroke-width="1.5"/></svg>
  Data Migrations</div>

<h2 class="abs section-title" style="left:52px;top:563px">Industries</h2>
<ul class="abs list" style="left:52px;top:599px">
  <li>New Media (WEB,Mobile,TV)</li><li>Broadcast</li><li>Hospitality</li><li>Accounting</li><li>Central/Local Government</li><li>Pharmaceuticals</li><li>Technology Start Up's</li>
</ul>
<h2 class="abs section-title" style="left:282px;top:563px">Business Functions</h2>
<ul class="abs list" style="left:282px;top:599px">
  <li>Contract Management</li><li>Treasury Management</li><li>Document Management</li><li>Payment Services (Swift/EDI)</li><li>Insurance Risk Management</li><li>Maintenance Management Systems</li><li>ERP/CRM</li><li>Content Management</li><li>eCommerce</li>
</ul>

<aside class="abs demo">
  <h3>Request Demo</h3>
  <p class="lead">Feel free to get in touch with Request Demo Enquiries. we are here to help !</p>
  <div class="demo-card">
    <div class="field" style="top:15px">YOUR NAME</div>
    <div class="field" style="top:47px">YOUR EMAIL</div>
    <div class="field" style="top:80px">SERVICE TYPE<span class="caret"></span></div>
    <p class="demo-note">Fill out the form above to recieve a free and confidential intial consultation. Don't worry, we never share your information or use it to spam you.</p>
    <div class="demo-btn">SEND YOUR REQUEST</div>
  </div>
</aside>

<section class="abs contact">
  <div class="contact-item" style="left:53px"><i>Call Us Now !</i><strong>+44 (0) 8000 5550 12</strong><span>24/7 Available</span></div>
  <div class="contact-item" style="left:198px"><i>Send Us Message</i><strong>contact@hartsys.example</strong><span>24/7 Available</span></div>
  <div class="contact-item" style="left:349px"><i>Visit Our Office !</i><strong>Northgate House, 4th Floor, London, UK</strong><a>View Map</a></div>
</section>

<footer class="abs footer"></footer>
<div class="abs foot-brand">HARTWELL<small>SYSTEMS ADVISORY</small></div>
<p class="abs foot-about">Lorem ipsum dolor sit amet, consectetur adipiscing elit, sed do eiusmod tempor incididunt ut labore et dolore magna aliqua. Ut enim ad minim veniam, quis nostrud exercitation ullamco laboris nisi ut aliquip ex ea commodo consequat.</p>

<h4 class="abs foot-h" style="left:198px;top:961px">Business Hours</h4>
<div class="abs foot-text" style="left:198px;top:981px">Opening Days :<span class="hi">Monday - Friday : 9 AM to 21 PM</span><span class="hi">Saturday : 9 AM to 15 PM</span><br>Vacations :<span class="hi">All Sunday Days</span><span class="hi">All Official Holidays</span></div>

<h4 class="abs foot-h" style="left:350px;top:961px">Corporate Info</h4>
<ul class="abs links" style="left:350px;top:981px">
  <li>Home</li><li>Services</li><li>Brevanta Solutions</li><li>Portfolio</li><li>Clients</li><li>Blog</li><li>Contact Us</li><li>Request Demonstration</li>
</ul>

<h4 class="abs foot-h" style="left:494px;top:961px">Blog &amp; News</h4>
<div class="abs" style="left:494px;top:981px">
  <div class="news"><div class="date">25 Feb<small>2016</small></div><p>Brevanta UK Reseller Agreement Announcement</p></div>
  <div class="news"><div class="date">17 Jan<small>2016</small></div><p>New Web Site, Branding and SecureMark and SSL Security</p></div>
</div>

<p class="abs copyright">Copyright © 2016 Hartwell Systems Advisory Ltd.</p>
<div class="abs badge" style="left:506px;top:1123px;width:66px;height:15px"></div>
<div class="abs badge" style="left:579px;top:1122px;width:50px;height:28px"></div>

</body>
</html>
```